Content marketing firm needs a creative out of the box stationary design

Please take a look to the uploaded logo
I need the whole stationary package which include designs for (business card, letterhead, folder, notepad, company profile, small and big envelop, CD and its cover, key medal, header cover for social media pages "facebook, twitter, linkedin, insgram, google+" and website, favicon for website, E-mail signature, flyer, brochure)
Business

```html
<!DOCTYPE html>
<html lang="en">
<head>
<meta charset="utf-8">
<title>Brightleaf Media – Business Card</title>
<link rel="stylesheet" href="https://fonts.googleapis.com/css2?family=Open+Sans:wght@400;700;800&family=Arimo:wght@400;700&display=swap">
<style>
  :root {
    --backdrop: #e4e6e8;
    --brand-blue: #1e8bbf;
    --accent-blue: #1ea0dc;
    --ink: #1d1d1f;
    --text: #2a2a2a;
    --muted: #555a5e;
    --paper: #ffffff;
    --strip-dark: #262626;
  }
  * { box-sizing: border-box; margin: 0; padding: 0; }
  html, body {
    width: 1200px; height: 1000px; overflow: hidden;
    background: var(--backdrop);
  }
  .stage {
    width: 1200px; height: 1000px;
    display: flex; flex-direction: column;
    align-items: center; justify-content: center; gap: 56px;
  }
  .card {
    position: relative;
    width: 700px; height: 400px;
    overflow: hidden;
    box-shadow: 0 10px 30px rgba(0,0,0,0.12);
  }
  /* Front */
  .card--front {
    background: var(--brand-blue);
    display: flex; align-items: center; justify-content: center;
  }
  .brand-name {
    font-family: "Open Sans", sans-serif;
    font-weight: 800;
    letter-spacing: 1px;
    text-transform: uppercase;
  }
  .card--front .brand-name {
    font-size: 54px; color: var(--ink);
  }
  /* Back */
  .card--back { background: var(--paper); }
  .card__edge { position: absolute; inset: 0; }
  .card--back .brand-name {
    position: absolute; left: 70px; top: 72px;
    font-size: 32px; color: var(--ink);
  }
  .contact {
    position: absolute; left: 390px; top: 150px;
    font-family: "Arimo", sans-serif; color: var(--text);
  }
  .contact__name {
    font-weight: 700; font-size: 21px; letter-spacing: 1px;
    color: var(--accent-blue); text-transform: uppercase;
  }
  .contact__role { font-size: 14px; color: var(--muted); margin-bottom: 14px; }
  .contact__list { list-style: none; }
  .contact__item {
    display: flex; align-items: center; gap: 9px;
    font-size: 15px; line-height: 24px;
  }
  .contact__icon { width: 16px; height: 16px; flex: none; }
  .contact__address { margin-top: 12px; font-size: 15px; line-height: 22px; font-style: normal; }
</style>
</head>
<body>
<main class="stage">
  <section class="card card--front" aria-label="Business card front">
    <p class="brand-name">Brightleaf Media</p>
  </section>

  <section class="card card--back" aria-label="Business card back">
    <svg class="card__edge" width="700" height="400" viewBox="0 0 700 400" aria-hidden="true">
      <polygon points="0,0 14,0 14,360 0,360" fill="var(--strip-dark)"/>
      <polygon points="0,352 0,400 700,400 700,372 270,372 250,352" fill="var(--accent-blue)"/>
    </svg>

    <p class="brand-name">Brightleaf Media</p>

    <div class="contact">
      <p class="contact__name">Jordan Ellis</p>
      <p class="contact__role">Managing Director</p>
      <ul class="contact__list">
        <li class="contact__item">
          <svg class="contact__icon" viewBox="0 0 16 16" aria-hidden="true"><rect width="16" height="16" rx="3" fill="var(--accent-blue)"/><path d="M5 3.5l2 2-1 1.3c.7 1.4 1.8 2.5 3.2 3.2l1.3-1 2 2-1.3 1.5C8 12.3 3.7 8 3.5 4.8z" fill="#fff"/></svg>
          +61 800 555 0199
        </li>
        <li class="contact__item">
          <svg class="contact__icon" viewBox="0 0 16 16" aria-hidden="true"><rect width="16" height="16" rx="3" fill="var(--accent-blue)"/><rect x="3" y="4.5" width="10" height="7" fill="none" stroke="#fff" stroke-width="1.2"/><path d="M3 4.5l5 4 5-4" fill="none" stroke="#fff" stroke-width="1.2"/></svg>
          hello@brightleaf-media.com
        </li>
        <li class="contact__item">
          <svg class="contact__icon" viewBox="0 0 16 16" aria-hidden="true"><rect width="16" height="16" rx="3" fill="var(--accent-blue)"/><circle cx="8" cy="8" r="4.8" fill="none" stroke="#fff" stroke-width="1.1"/><path d="M3.2 8h9.6M8 3.2c-2 2.6-2 7 0 9.6M8 3.2c2 2.6 2 7 0 9.6" fill="none" stroke="#fff" stroke-width="1"/></svg>
          www.brightleaf-media.com
        </li>
      </ul>
      <address class="contact__address">18 Harbor Lane<br>Fairview, CA 90010</address>
    </div>
  </section>
</main>
</body>
</html>
```